Keystone Institute Logo & Business card

Keystone Institute - Professional ICT Training
business is a training center.
Logo and business card that have an ID.
bold publicity, distinct, and prestige image
"Ensure professional Success"
that will attract target customer to come and take a look. that will look prestige on certificate after graduation, that will serve as a business tool to attract Business and enterprise customer (let them send their staff for training)

Target Market(s)

young professionals, university students, youth building career in IT fields

Industry/Entity Type

Education

Contact Information for Business Card

Font styles to use
Sans Serif

Colors

Designer to choose colors to be used in the design.

Requirements
Must have
• Logo Identity
• uniqueness
Nice to have
• catch phrase or illustration
Should not have
• just use alphabet as logo.

```html
<!DOCTYPE html>
<html lang="en">
<head>
<meta charset="utf-8">
<title>Keystone Institute – Business Card</title>
<link rel="stylesheet" href="https://fonts.googleapis.com/css2?family=Lato:wght@400;900&family=Orbitron:wght@800&display=swap">
<style>
  :root {
    --navy: #142c52;
    --navy-deep: #1c1f52;
    --orange: #f5a623;
    --white: #ffffff;
    --grey-text: #6d6f73;
    --backdrop: #1b1b1d;
  }
  * { box-sizing: border-box; margin: 0; padding: 0; }
  html, body {
    width: 1200px; height: 1189px; overflow: hidden;
    background: var(--backdrop);
    font-family: "Lato", sans-serif;
  }
  .canvas {
    position: relative; width: 1200px; height: 1189px;
  }
  .card {
    position: absolute; left: 145px; width: 910px; height: 520px;
    border-radius: 30px; overflow: hidden;
  }
  .card--front { top: 40px; background: var(--navy); }
  .card--back { top: 629px; background: var(--white); }

  /* Brand lockup */
  .brand { position: absolute; text-align: right; }
  .brand__mark {
    display: inline-block; width: 34px; height: 34px;
    background: var(--orange); border-radius: 6px;
    margin-bottom: 14px;
  }
  .brand__name {
    font-family: "Lato", sans-serif; font-weight: 900;
    font-size: 52px; letter-spacing: 1px; text-transform: uppercase;
    line-height: 1;
  }
  .brand__tagline {
    font-family: "Lato", sans-serif; font-weight: 400;
    font-size: 20px; letter-spacing: 6px; color: var(--orange);
    margin-top: 8px;
  }
  .card--front .brand {
    left: 0; right: 0; top: 170px; text-align: center;
  }
  .card--front .brand__name { color: var(--white); }
  .card--back .brand { right: 60px; top: 60px; }
  .card--back .brand__name { color: var(--navy); font-size: 44px; }
  .card--back .brand__tagline { font-size: 17px; letter-spacing: 5px; }

  /* Divider */
  .divider {
    position: absolute; left: 70px; right: 60px; top: 262px;
    height: 2px; background: var(--orange);
  }

  /* Person */
  .person { position: absolute; left: 70px; top: 190px; }
  .person__name {
    font-family: "Orbitron", sans-serif; font-weight: 800;
    font-size: 30px; color: var(--navy); text-transform: uppercase;
    letter-spacing: 1px;
  }
  .person__role {
    font-size: 24px; color: var(--orange); margin-top: 2px;
  }

  /* Contact list */
  .contact { position: absolute; left: 70px; top: 292px; list-style: none; }
  .contact__item {
    display: flex; align-items: center; gap: 16px;
    font-size: 25px; color: var(--grey-text); line-height: 40px;
  }
  .contact__icon { width: 22px; height: 22px; flex: none; }

  .address {
    position: absolute; right: 60px; top: 292px; text-align: right;
    font-size: 24px; color: var(--grey-text); line-height: 34px;
  }

  /* Bottom band */
  .band {
    position: absolute; left: 0; right: 0; bottom: 0; height: 16px;
    display: flex;
  }
  .band__navy { flex: 1; background: var(--navy-deep); }
  .band__accent { width: 150px; background: var(--orange); }
</style>
</head>
<body>
<main class="canvas">

  <section class="card card--front" aria-label="Card front">
    <div class="brand">
      <span class="brand__mark" aria-hidden="true"></span>
      <div class="brand__name">Keystone Institute</div>
      <div class="brand__tagline">Professional ICT Training</div>
    </div>
  </section>

  <section class="card card--back" aria-label="Card back">
    <div class="brand">
      <span class="brand__mark" aria-hidden="true"></span>
      <div class="brand__name">Keystone Institute</div>
      <div class="brand__tagline">Professional ICT Training</div>
    </div>

    <div class="person">
      <div class="person__name">Maya Lindqvist</div>
      <div class="person__role">Director</div>
    </div>

    <div class="divider"></div>

    <ul class="contact">
      <li class="contact__item">
        <svg class="contact__icon" viewBox="0 0 22 22" aria-hidden="true">
          <rect x="5" y="2" width="12" height="18" rx="2" fill="none" stroke="#f5a623" stroke-width="2"/>
          <rect x="9" y="16" width="4" height="1.5" fill="#f5a623"/>
        </svg>
        (555) 218 0447
      </li>
      <li class="contact__item">
        <svg class="contact__icon" viewBox="0 0 22 22" aria-hidden="true">
          <rect x="2" y="5" width="18" height="12" fill="#f5a623"/>
          <path d="M2 5 L11 12 L20 5" fill="none" stroke="#ffffff" stroke-width="1.5"/>
        </svg>
        hello@keystonemail.com
      </li>
      <li class="contact__item">
        <svg class="contact__icon" viewBox="0 0 22 22" aria-hidden="true">
          <circle cx="11" cy="11" r="9" fill="none" stroke="#f5a623" stroke-width="2"/>
          <ellipse cx="11" cy="11" rx="4" ry="9" fill="none" stroke="#f5a623" stroke-width="1.5"/>
          <line x1="2" y1="11" x2="20" y2="11" stroke="#f5a623" stroke-width="1.5"/>
        </svg>
        www.keystoneweb.com
      </li>
    </ul>

    <address class="address" style="font-style: normal;">
      PO BOX 48, Harbour Lane<br>
      2nd street Geelong
    </address>

    <div class="band" aria-hidden="true">
      <span class="band__navy"></span>
      <span class="band__accent"></span>
    </div>
  </section>

</main>
</body>
</html>
```